Property Maintenance company needs a noticeable Car Wrap design

We need an outstanding car wrap design for our Kelvane Orca Tradelink Metro 2020. It needs to emphasize that our property maintenance company serves both Commercial and Residential clients. The wrap should communicate friendliness and quality services. I have attached a pdf file that outlines all the requirements for the wrap design. I also attached all relevant pictures to help with the creation of the design. The selected winner will receive the source files of the company logo & QTC logo to use in the car wrap design. I look forward to seeing all your designs!

Thank you!
Updates

Need extra days to review

Target Market(s)

Property Maintenance
Residential homeowners
Building owners

Industry/Entity Type

Property Maintenance

Requirements
Must have
• See Instruction file for all details.
Nice to have
• Some small icons that represent electrical, plumbing, handyman, and carpentry work.
For example, like a lightbulb, plug, or pipe icon. Or all of them. Try to use intuitive icons so the general public will know what it is.

Thanks!

```html
<!DOCTYPE html>
<html lang="en">
<head>
<meta charset="utf-8">
<title>Brightside Maintenance Services – Van Wrap</title>
<link rel="stylesheet" href="https://fonts.googleapis.com/css2?family=Montserrat:wght@600;800&family=Oswald:wght@500&display=swap">
<style>
  :root{
    --wrap-green:#6ab845;
    --wrap-navy:#2d3b8e;
    --wrap-blue:#5776b8;
    --wrap-grey:#d9dadb;
    --wrap-white:#ffffff;
    --trim-dark:#2b2b2b;
    --glass:#8d8f92;
    --hub:#8a8c8f;
  }
  html,body{margin:0;padding:0;background:var(--wrap-white);}
  body{width:1200px;height:1131px;overflow:hidden;}
  .wrap-sheet{display:block;width:1200px;height:1131px;}
  .brand-name{font-family:"Montserrat",sans-serif;font-weight:600;font-size:54px;fill:var(--wrap-navy);letter-spacing:1px;}
  .brand-tagline{font-family:"Montserrat",sans-serif;font-weight:600;font-size:14px;fill:var(--wrap-blue);letter-spacing:7px;}
  .phone{font-family:"Montserrat",sans-serif;font-weight:800;font-size:56px;fill:var(--wrap-blue);stroke:var(--wrap-white);stroke-width:5px;paint-order:stroke;}
  .web-band{fill:var(--wrap-blue);}
  .web-address{font-family:"Oswald",sans-serif;font-weight:500;font-size:22px;fill:#eef1f6;letter-spacing:.3px;}
  .service-line{font-family:"Montserrat",sans-serif;font-weight:600;font-size:13px;fill:var(--wrap-white);}
  .service-icon{fill:none;stroke:var(--wrap-white);stroke-width:1.6;}
</style>
</head>
<body>
<svg class="wrap-sheet" viewBox="0 0 1200 1131" xmlns="http://www.w3.org/2000/svg">
  <defs>
    <clipPath id="van-body-clip">
      <path d="M60,300 C75,278 160,256 300,246 L420,120 Q440,104 480,100 L1050,68 Q1086,70 1092,112 L1102,300 L1116,420 L1110,442 L62,446 Q40,420 46,340 Z"/>
    </clipPath>
    <g id="van-side">
      <g clip-path="url(#van-body-clip)">
        <rect class="panel-base" x="0" y="0" width="1200" height="500" fill="var(--wrap-grey)"/>
        <path class="panel-green" d="M0,0 L733,0 L733,70 C690,150 620,220 560,256 L60,362 L0,380 Z" fill="var(--wrap-green)"/>
        <path class="panel-navy" d="M455,460 C470,400 520,350 600,330 L1120,255 L1120,460 Z" fill="var(--wrap-navy)"/>
        <rect class="bumper-rear" x="1075" y="290" width="45" height="160" fill="var(--trim-dark)"/>
        <path class="bumper-front" d="M40,340 Q60,330 80,345 L85,450 L40,450 Z" fill="var(--trim-dark)"/>
      </g>
      <path class="side-window" role="img" aria-label="Cab side window" d="M345,240 L428,124 Q438,116 452,115 L553,113 L548,238 Z" fill="var(--glass)"/>
      <g class="wheel-front" role="img" aria-label="Front wheel">
        <circle cx="200" cy="440" r="74" fill="var(--wrap-white)"/>
        <circle cx="200" cy="440" r="68" fill="var(--trim-dark)"/>
        <circle cx="200" cy="440" r="44" fill="var(--hub)"/>
      </g>
      <g class="wheel-rear" role="img" aria-label="Rear wheel">
        <circle cx="967" cy="440" r="74" fill="var(--wrap-white)"/>
        <circle cx="967" cy="440" r="68" fill="var(--trim-dark)"/>
        <circle cx="967" cy="440" r="44" fill="var(--hub)"/>
      </g>
    </g>
  </defs>

  <!-- Driver side, facing left -->
  <g class="van van--driver-side">
    <use href="#van-side"/>
    <g class="web-stripe" transform="translate(290,396) rotate(-21)">
      <rect class="web-band" x="0" y="-26" width="280" height="32" rx="8"/>
      <text class="web-address" x="12" y="-2" textLength="256" lengthAdjust="spacingAndGlyphs">WWW.BRIGHTSIDEUPKEEP.COM</text>
    </g>
    <rect class="brand-mark" x="620" y="130" width="16" height="16" fill="var(--wrap-navy)"/>
    <text class="brand-name" x="645" y="180">BRIGHTSIDE</text>
    <text class="brand-tagline" x="635" y="214">MAINTENANCE SERVICES</text>
    <text class="phone" x="620" y="292">555-014-2290</text>
    <g class="service" transform="translate(601,362)">
      <circle class="service-icon" r="14"/>
      <path class="service-icon" d="M-6,6 L5,-5 M2,-8 Q8,-8 8,-2"/>
    </g>
    <text class="service-line" x="632" y="356">GENERAL MAINTENANCE/</text>
    <text class="service-line" x="632" y="373">HANDYMAN REPAIRS</text>
    <g class="service" transform="translate(601,409)">
      <circle class="service-icon" r="14"/>
      <path class="service-icon" d="M-7,1 L0,-6 L7,1 M-5,0 L-5,7 L5,7 L5,0"/>
    </g>
    <text class="service-line" x="632" y="403">COMMERCIAL &amp; RESIDENTIAL</text>
    <text class="service-line" x="632" y="420">RENOVATIONS</text>
  </g>

  <!-- Passenger side, facing right -->
  <g class="van van--passenger-side">
    <use href="#van-side" transform="translate(1170,553) scale(-1,1)"/>
    <g class="web-stripe" transform="translate(618,849) rotate(21)">
      <rect class="web-band" x="0" y="-26" width="280" height="32" rx="8"/>
      <text class="web-address" x="12" y="-2" textLength="256" lengthAdjust="spacingAndGlyphs">WWW.BRIGHTSIDEUPKEEP.COM</text>
    </g>
    <rect class="brand-mark" x="145" y="683" width="16" height="16" fill="var(--wrap-navy)"/>
    <text class="brand-name" x="170" y="733">BRIGHTSIDE</text>
    <text class="brand-tagline" x="145" y="767">MAINTENANCE SERVICES</text>
    <text class="phone" x="120" y="845">555-014-2290</text>
    <g class="service" transform="translate(342,903)">
      <circle class="service-icon" r="14"/>
      <path class="service-icon" d="M-6,6 L5,-5 M2,-8 Q8,-8 8,-2"/>
    </g>
    <text class="service-line" x="373" y="897">GENERAL MAINTENANCE/</text>
    <text class="service-line" x="373" y="914">HANDYMAN REPAIRS</text>
    <g class="service" transform="translate(342,952)">
      <circle class="service-icon" r="14"/>
      <path class="service-icon" d="M-7,1 L0,-6 L7,1 M-5,0 L-5,7 L5,7 L5,0"/>
    </g>
    <text class="service-line" x="373" y="946">COMMERCIAL &amp; RESIDENTIAL</text>
    <text class="service-line" x="373" y="963">RENOVATIONS</text>
  </g>
</svg>
</body>
</html>
```